Business Card Design Project

Hello- I am an interior stylist/product designer whose work is detail driven, very clean and transitional in style and I want my business card to reflect those qualities. I have a logo that I use on my website- my name and a hand drawn chandelier that I want incorporated into the design. However, "Design for the Home" needs to be changed to "Designs". I will be using cream colored stock and am thinking of gray text and logo. I need your help in pulling my card together since it will be the most used element and drive the design of the rest of my stationary suite.
Updates

Please note that I have changed my QR code from my cell # to my website. The new code will be downloaded now.

Reason: I want to thank everyone who has submitted designs- there are truly some very inspiring designs and I am very pleased. I want to make certain that I get this right and have an attractive and highly effective marketing tool when we are finished. With that said, I have run into a technical problem with one aspect of the card- a qr code for my website that was not part of the original brief. I will get that corrected today and post. Once I get that taken care of, I will post comments to all designs received do far. Thanks again for everyone's efforts, Risa

QR Code for the website is now uploaded. Thanks for your patience!

Target Market(s)

Upper middle class- mostly women

Industry/Entity Type

Business

Requirements
Must have
• Marisa Vantry Designs
"...to the last detail."
214-555-0148
marisavantry@plumwick.net
www.marisavantrydesigns-example.com
27083 Birchmont Court
Dallas, TX 75000
Nice to have
• Risa Vantry
Owner

```html
<!DOCTYPE html>
<html lang="en">
<head>
<meta charset="utf-8">
<title>Marisa Vantry Designs – Business Cards</title>
<link rel="stylesheet" href="https://fonts.googleapis.com/css2?family=EB+Garamond:ital,wght@0,400;0,600;1,400&family=Arimo:wght@400&display=swap">
<style>
  :root {
    --backdrop: #e4e4e4;
    --card: #ffffff;
    --ink: #4a4a4a;
    --ink-soft: #5e5e5e;
    --rule: #8a8a8a;
    --art-tone: #b9b9b9;
    --card-edge: #d2d2d2;
  }
  * { margin: 0; padding: 0; box-sizing: border-box; }
  html, body { width: 1200px; height: 900px; overflow: hidden; }
  body { background: var(--backdrop); position: relative; font-family: "EB Garamond", Georgia, serif; color: var(--ink); }

  .card { position: absolute; width: 708px; background: var(--card); border: 1px solid var(--card-edge); }
  .card--front { left: 27px; top: 27px; height: 411px; }
  .card--back { left: 465px; top: 462px; height: 408px; }

  .mark-art { position: absolute; background: var(--art-tone); }
  .card--front .mark-art { left: 263px; top: 63px; width: 190px; height: 222px; }
  .card--back .mark-art { left: 312px; top: 40px; width: 96px; height: 126px; }

  .brand-name { position: absolute; display: flex; justify-content: space-between; font-family: "EB Garamond", Georgia, serif; font-weight: 400; color: var(--ink); line-height: 1; }
  .card--front .brand-name { left: 92px; width: 530px; top: 238px; font-size: 62px; }
  .card--back .brand-name { left: 228px; width: 262px; top: 134px; font-size: 31px; }

  .tagline { position: absolute; left: 0; width: 100%; text-align: center; font-family: "Arimo", Arial, sans-serif; color: var(--ink-soft); text-transform: uppercase; }
  .card--front .tagline { top: 318px; font-size: 21px; letter-spacing: 4px; }
  .card--back .tagline { top: 177px; font-size: 12.5px; letter-spacing: 2.4px; }

  .motto { position: absolute; left: 0; width: 100%; top: 352px; text-align: center; font-family: "EB Garamond", Georgia, serif; font-style: italic; font-size: 20px; color: var(--ink-soft); }

  .divider { position: absolute; left: 78px; top: 222px; width: 552px; height: 24px; }

  .owner { position: absolute; left: 52px; top: 270px; }
  .owner-name { font-size: 19px; font-weight: 600; letter-spacing: 1.5px; text-transform: uppercase; color: var(--ink); }
  .owner-role { font-size: 16px; color: var(--ink-soft); margin-top: 2px; }

  .contact { position: absolute; right: 42px; top: 300px; text-align: right; font-size: 16px; line-height: 24px; color: var(--ink); font-style: normal; }
</style>
</head>
<body>
  <section class="card card--front" aria-label="Business card front">
    <div class="mark-art" role="img" aria-label="Hand-drawn three-arm chandelier illustration in graphite gray"></div>
    <div class="brand-name"><span>Marisa</span><span>Vantry</span></div>
    <p class="tagline">Designs</p>
    <p class="motto">...to the last detail.</p>
  </section>

  <section class="card card--back" aria-label="Business card back">
    <div class="mark-art" role="img" aria-label="Hand-drawn three-arm chandelier illustration in graphite gray"></div>
    <div class="brand-name"><span>Marisa</span><span>Vantry</span></div>
    <p class="tagline">Designs</p>

    <svg class="divider" viewBox="0 0 552 24">
      <line x1="6" y1="12" x2="546" y2="12" stroke="var(--rule)" stroke-width="2"/>
      <polygon points="0,12 8,8 8,16" fill="var(--rule)"/>
      <polygon points="552,12 544,8 544,16" fill="var(--rule)"/>
      <rect x="246" y="4" width="60" height="16" fill="var(--art-tone)" role="img" aria-label="Small scrolled centre flourish"/>
    </svg>

    <div class="owner">
      <p class="owner-name">Risa Vantry</p>
      <p class="owner-role">Owner</p>
    </div>

    <address class="contact">
      <p>www.marisavantrydesigns-example.com</p>
      <p>27083 Birchmont Court, Dallas, TX 75000</p>
      <p>214-555-0148 &nbsp;|&nbsp; marisavantry@plumwick.net</p>
    </address>
  </section>
</body>
</html>
```